I need a label design for Honey

Tropical Theme Logo designed for a Beekeeping Company.
5 Labels for Honey.
Business Cards
“Sun Orchard”

A Tropical themed logo, either palm tree or bee.

Style of text should be Brush Script italic or something tropical similar.

I like the below style, with no flamingos or pineapples . Colorful and leafy is good, preferably with leaves and flowers that are native to Tropical Queensland Australia.

Label 1. 1 kg rainforest Blend

This will be our standard table honey, I would like to have a vey striking colorful, cheerful design something like to the 2 examples above.

Must have Australian made logo on Side 2 , with words Australian Honey in it. See attached Australian made logo pick either portrait or landscape based on your design.

If you think the attached picture of the Pink Euodia is will help the labels appeal please feel free to use it.
Please See attached Document for content rainforest Honey Label 1 kg.

Barcode 0918273645501

Size of labels ae shown below. I would like 5mm radius on all corners. 15 mm allowance for curvature of bottle.
Side 1 Side 2 Side 3

65mm

Label 2. 1 kg Bloodwood and Scarlet Gum Blend

This will be another of our standard table honey, I would like to have a vey striking colorful, cheerful design something like to the 2 examples above.

Must have Australian made logo on Side 2 , with words Australian Honey in it. See attached Australian made logo pick either portrait or landscape based on your design

If you think the attached picture of the Scarlet Gum is will help the labels appeal please feel free to use it.

Please See attached Document for content Bloodwood and Scarlet Gum Blend Label 1 kg.
Barcode 0918273645518
Side 1 Side 2 Side 3

65mm

Label 3. 500 g rainforest Blend

Exactly the same as the 1 kg rainfest blend but the Net weight ill be changed to 500 grams.

If you think the attached picture of the Pink Euodia is ill help the labels appeal please feel free to use it.
Barcode 0918273645525
Side 1 Side 2 Side 3

65mm

Label 4. 500g Bloodwood and Scarlet Gum Blend

Exactly the same as the 1 kg “Bloodwood and Scarlet Gum Blend” but the Net weight ill be changed to 500 grams.

Barcode 0918273645532
Side 1 Side 2 Side 3

65mm

Label 5. 250g Manuka Honey Attached rough word document for layout and text

This will be our Sun Orchard Premium range of Honeys, A bonze, theme to denote the quality of honey. Printed on silver backed label paper, to give it a shiny appearance.

Main Points
• Bronze backing, see picture below for example from competitor.
• Silver backed labels paper.
• Must have the Australian made Logo on the Front of jar or side 2.
• Side 1 Australian map outline in the bronze backing color with a arrow to Cairns.
• Side 2 has logo “Sun Orchard” Name, Australian Manuka Honey, Leptospermum Polygalifolium Tropicum, Australian Made Logo (Australian Honey) see file “GrownProducedMade_PDF_P (1).pdf”, 250g, NPA+8, MGO 183
• Side 3 TEXT “Our Australian Manuka honey is sourced from pristine native leptospermum forests situated in tropical north Queensland.

Manuka honey gets it’s unique antibacterial properties from naturally occurring methylglyoxal (MGO). The higher the MGO rating the stronger antibacterial properties.”
• Side 4 Nutritional Information Table, Address, Barcode” 0918273645549”, Text “recycled container “with recycled logo

Barcode 0918273645549
First 3 side connected with 6 mm allowance for curvature of bottle, Side 4 separate. 5mm radius on all corners
Side 1 Side 2 Side 3 Side 4

50mm

Competitors labels for inspiration and example of Bronze Backing

*Business Card*
Sun Orchard “logo”

Medical Honey’s
Tropical Rainforest Honeys
Strong 5 Fames Nucleus Colonies all year round
Director Rupert Vasquez
Email: rvasquez.rv@examplemail.test
Mobile no. 0491 058 273
ABN 71596204318

Target Market(s)

Tourist visiting Cairns North Queensland Australia, both foreign mainly Chinese and tourist from Melbourne.

Contact Information for Business Card

Sun Orchard “logo”

Medical Honey’s
Tropical Rainforest Honey's
Director Rupert Vasquez
Mobile no. 0491 058 273
ABN 71596204318

Logo Text

Sun Orchard

Font styles to use
Script

Colors
00a990
f04a50
0255a3
9bcb3b
fbed22

Requirements
Must have
• Clean and Clear, must check all spelling, punctuation and Gram
Nice to have
• Lots of colour in labels but not too much content.
• O
• Manuka labels to be high end looking people are paying good money and should see it in the label.
• Other honey ranges can be colourful and playful. Topical relaxed, rainforest

```html
<!DOCTYPE html>
<html lang="en">
<head>
<meta charset="utf-8">
<title>Sun Orchard – Honey Label and Business Cards</title>
<link href="https://fonts.googleapis.com/css2?family=Courgette&family=Ubuntu:wght@300;400;500;700&family=Arimo:wght@400;700&display=swap" rel="stylesheet">
<style>
  :root{
    --page:#ffffff;
    --plum:#8b2d5e;
    --brand:#6b3d1e;
    --maroon:#8a2a1e;
    --leaf:#2f9e44;
    --leaf-dark:#1f6e2e;
    --leaf-light:#9bcb3b;
    --map:#3cb44b;
    --pin:#f04a50;
    --teal:#0aa68a;
    --cream:#fbf8d8;
    --flower:#b2629a;
    --flower-light:#d9a6c9;
    --ink:#1a1a1a;
    --rule:#222222;
  }
  *{box-sizing:border-box;margin:0;padding:0}
  html,body{width:1200px;height:901px;overflow:hidden;background:var(--page)}
  body{position:relative;font-family:"Ubuntu",sans-serif;color:var(--ink)}

  .brand-name{font-family:"Courgette",cursive;color:var(--brand);font-weight:400;white-space:nowrap}

  /* ---------- business cards ---------- */
  .card{position:absolute;width:266px;height:172px;background:#fff;box-shadow:0 2px 8px rgba(0,0,0,.18);overflow:hidden}
  .card--front{left:812px;top:100px}
  .card--back{left:812px;top:310px;display:flex}

  .foliage{position:absolute;z-index:1;background:radial-gradient(ellipse at center,var(--leaf) 0%,var(--leaf-light) 55%,rgba(155,203,59,0) 72%)}
  .foliage--dark{background:radial-gradient(ellipse at center,var(--leaf-dark) 0%,var(--leaf) 50%,rgba(47,158,68,0) 72%)}

  .card__identity{position:absolute;z-index:2;left:0;right:0;top:52px;text-align:center}
  .card__identity .brand-name{font-size:22px;line-height:1}
  .tagline-main{font-weight:700;color:var(--maroon);font-size:7px;margin-top:12px}
  .tagline-sub{font-size:7px;color:var(--maroon);margin-top:3px}
  .tagline-small{font-size:5.6px;color:#8a6d16;margin-top:2px}

  .card__left{width:133px;height:100%;display:flex;flex-direction:column;align-items:center;justify-content:center;text-align:center}
  .card__left .brand-name{font-size:16px}
  .card__left .tagline-main{margin-top:9px;font-size:6.5px}
  .card__left .tagline-sub{font-size:6.5px}
  .card__left .tagline-small{font-size:3.6px}
  .card__right{flex:1;background:var(--teal);color:#fff;padding:58px 0 0 15px}
  .card__role{font-size:6.5px}
  .card__name{font-size:14px;font-weight:500;margin:3px 0 4px}
  .card__contact{font-size:6.5px;line-height:1.25}

  /* ---------- wrap label ---------- */
  .label{position:absolute;left:121px;top:522px;width:957px;height:277px;background:var(--cream);box-shadow:0 2px 8px rgba(0,0,0,.18);overflow:hidden}
  .label__panel{position:absolute;top:0;height:100%;background:#fff}
  .panel--story{left:0;width:267px}
  .panel--nutrition{left:719px;width:238px}
  .panel--front{left:347px;top:8px;width:262px;height:262px;z-index:2;background:#fff;box-shadow:0 0 0 1px #eee;text-align:center}

  .map{position:absolute;z-index:3;left:39px;top:18px;width:126px;height:124px;background:var(--map);border-radius:38% 46% 40% 42%}
  .pin{position:absolute;z-index:4;left:126px;top:16px}

  .story{position:absolute;z-index:3;left:40px;top:158px;width:208px;font-size:9.6px;font-weight:300;line-height:12.6px}
  .story b{font-weight:700}

  .panel--front .brand-name{display:block;font-size:19px;margin-top:28px}
  .product-title{font-family:"Courgette",cursive;color:var(--plum);font-size:23px;line-height:28px;font-weight:400;margin-top:18px}
  .flower{position:absolute;left:90px;top:147px;width:88px;height:88px;border-radius:50%;background:radial-gradient(circle at 45% 40%,var(--flower-light) 0%,var(--flower) 55%,rgba(178,98,154,0) 72%)}
  .origin-badge{position:absolute;left:56px;top:182px;width:34px;height:48px;border:2px solid var(--leaf);border-radius:3px;background:#fff}
  .origin-badge::before{content:"";position:absolute;left:4px;top:4px;right:4px;height:24px;background:var(--leaf);border-radius:2px}
  .net-weight{position:absolute;left:0;right:0;bottom:14px;font-size:10px}

  .nutrition{position:absolute;z-index:3;left:15px;top:14px;width:170px;border:1px solid var(--rule);background:#fff;font-family:"Arimo",sans-serif;font-size:7.4px;line-height:9px}
  .nutrition__head{padding:1px 8px 3px;border-bottom:1px solid var(--rule)}
  .nutrition__head strong{display:block;font-size:8px}
  .nutrition table{width:100%;border-collapse:collapse}
  .nutrition td,.nutrition th{font-weight:400;border-bottom:1px solid var(--rule);padding:0 2px}
  .nutrition td:nth-child(2),.nutrition td:nth-child(3),.nutrition th:nth-child(2),.nutrition th:nth-child(3){border-left:1px solid var(--rule);text-align:center;width:40px}
  .nutrition th{height:24px}
  .nutrition .indent{padding-left:14px}
  .nutrition tr:last-child td{border-bottom:0}
  .footnote{position:absolute;z-index:3;left:15px;top:170px;font-family:"Arimo",sans-serif;font-size:7.2px;line-height:9px}
  .address{position:absolute;z-index:3;left:15px;top:200px;font-family:"Arimo",sans-serif;font-size:7.2px;line-height:9px}
  .recycle{position:absolute;z-index:3;left:100px;top:222px;text-align:center;font-family:"Arimo",sans-serif;font-size:8px;line-height:9px}
</style>
</head>
<body>

<!-- business card: front -->
<section class="card card--front">
  <div class="foliage" role="img" aria-label="Tropical leaf illustration, top left" style="left:-40px;top:-30px;width:140px;height:90px"></div>
  <div class="foliage foliage--dark" role="img" aria-label="Monstera leaf illustration, top" style="left:80px;top:-25px;width:80px;height:50px"></div>
  <div class="foliage" role="img" aria-label="Palm frond illustration, top right" style="right:-35px;top:-30px;width:120px;height:90px"></div>
  <div class="foliage" role="img" aria-label="Tropical leaf illustration, left side" style="left:-40px;top:90px;width:80px;height:110px"></div>
  <div class="foliage foliage--dark" role="img" aria-label="Monstera leaf illustration, bottom" style="left:40px;bottom:-30px;width:110px;height:60px"></div>
  <div class="foliage" role="img" aria-label="Tropical leaf illustration, bottom right" style="right:-30px;bottom:-40px;width:130px;height:90px"></div>
  <div class="card__identity">
    <div class="brand-name">Sun Orchard</div>
    <p class="tagline-main">Medical Honey's</p>
    <p class="tagline-sub">Tropical Rainforest Honeys</p>
    <p class="tagline-small">Strong 5 Fames Nucleus Colonies all year round</p>
  </div>
</section>

<!-- business card: back -->
<section class="card card--back">
  <div class="card__left">
    <div class="brand-name">Sun Orchard</div>
    <p class="tagline-main">Medical Honey's</p>
    <p class="tagline-sub">Tropical Rainforest Honeys</p>
    <p class="tagline-small">Strong 5 Fames Nucleus Colonies all year round</p>
  </div>
  <div class="card__right">
    <p class="card__role">Director</p>
    <p class="card__name">Rupert Vasquez</p>
    <p class="card__contact">rvasquez.rv@examplemail.test<br>0491 058 273<br>ABN 71596204318</p>
  </div>
</section>

<!-- wrap-around jar label -->
<section class="label">
  <div role="img" aria-label="Pale yellow chevron stripe pattern" style="position:absolute;inset:0;background:var(--cream)"></div>

  <div class="label__panel panel--story">
    <div class="map" role="img" aria-label="Green map of Australia"></div>
    <svg class="pin" width="16" height="22" viewBox="0 0 16 22" aria-hidden="true">
      <path d="M8 0a8 8 0 0 1 8 8c0 6-8 14-8 14S0 14 0 8a8 8 0 0 1 8-8z" fill="var(--pin)"/>
      <circle cx="8" cy="8" r="3.4" fill="#fff"/>
    </svg>
    <p class="story">Our bee are located neighboring the Daintree and Cedar Bay National Parks. The bees forage from these pristine untouched rainforest producing a unique mixed flora source honey. One unique flower is that of the <b>Pink Euodia</b>. The <b>Pink Euodia</b> is also the host tree of the Ulysses butterfly.</p>
  </div>

  <div class="label__panel panel--nutrition">
    <div class="nutrition">
      <div class="nutrition__head">
        <strong>NUTRITIONAL INFORMATION</strong>
        Serves per Jar: 17<br>Serving size: 15 g
      </div>
      <table>
        <tr><th></th><th>Per<br>Serve</th><th>Per 100g</th></tr>
        <tr><td>Energy</td><td>212kJ</td><td>1416 kJ</td></tr>
        <tr><td>Protein</td><td>0.05g</td><td>0.3g</td></tr>
        <tr><td>Fat - total</td><td>0g</td><td>0g</td></tr>
        <tr><td class="indent">- saturated</td><td>0g</td><td>0g</td></tr>
        <tr><td class="indent">- trans</td><td>0g</td><td>0g</td></tr>
        <tr><td>Cholesterol</td><td>0mg</td><td>0mg</td></tr>
        <tr><td>Carbohydrate</td><td>12.5g</td><td>83.1</td></tr>
        <tr><td class="indent">- Sugar*</td><td>12.4g</td><td>82.5</td></tr>
        <tr><td>Sodium</td><td>2.3mg</td><td>15mg</td></tr>
      </table>
    </div>
    <p class="footnote">*Sugars naturally occurring in honey<br>Ingredients:100% Pure Australian Honey</p>
    <p class="address">Lot 9 Coral Ridge Road,<br>Palmvale Australia 4870, +61 491058273</p>
    <div class="recycle">
      <svg width="32" height="28" viewBox="0 0 32 28" aria-hidden="true">
        <path d="M16 2 L30 26 H2 Z" fill="none" stroke="#111" stroke-width="2.4" stroke-linejoin="round"/>
        <text x="16" y="21" text-anchor="middle" font-family="Arimo, sans-serif" font-size="9" font-weight="700" fill="#111">02</text>
      </svg>
      <div>PE HD</div>
    </div>
  </div>

  <!-- foliage around the label edges, kept clear of the text blocks -->
  <div class="foliage" role="img" aria-label="Palm and monstera leaves along the top left edge" style="left:-30px;top:-30px;width:120px;height:60px"></div>
  <div class="foliage foliage--dark" role="img" aria-label="Tropical leaves along the top edge" style="left:180px;top:-35px;width:200px;height:65px"></div>
  <div class="foliage" role="img" aria-label="Palm fronds along the top edge" style="left:580px;top:-35px;width:150px;height:65px"></div>
  <div class="foliage" role="img" aria-label="Tropical leaves at the top right corner" style="left:905px;top:-30px;width:90px;height:60px"></div>
  <div class="foliage" role="img" aria-label="Tropical leaves at the bottom left" style="left:-40px;bottom:-40px;width:130px;height:66px"></div>
  <div class="foliage foliage--dark" role="img" aria-label="Tropical leaves at the bottom centre" style="left:270px;bottom:-45px;width:200px;height:90px"></div>
  <div class="foliage" role="img" aria-label="Tropical leaves at the bottom right of the front panel" style="left:520px;bottom:-45px;width:220px;height:90px"></div>
  <div class="foliage" role="img" aria-label="Tropical leaves at the bottom right" style="right:-40px;bottom:-40px;width:110px;height:66px"></div>

  <div class="label__panel panel--front">
    <span class="brand-name">Sun Orchard</span>
    <h1 class="product-title">Rainforest Mixed<br>Flora Source Honey</h1>
    <div class="flower" role="img" aria-label="Pink Euodia flower illustration"></div>
    <div class="origin-badge" role="img" aria-label="Country of origin badge"></div>
    <p class="net-weight">1 kg</p>
  </div>
</section>

</body>
</html>
```